Post Card Design Bright Path Youth

We need a postcard design that will be mailed to all residents offering free pickups of donated clothing. Our foundation is called Bright Path Youth, we are a nonprofit charitable organization that provides meals and medical services to children in need in Honduras. Collecting unwanted second-hand clothing generates revenue that helps fund the mission and programs run by our foundation. We would like to offer our pickup services to everyone who has any unwanted reusable clothing.

```html
<!DOCTYPE html>
<html lang="en">
<head>
<meta charset="utf-8">
<title>Bright Path Youth – Clothing Donation Postcard</title>
<link href="https://fonts.googleapis.com/css2?family=Lato:wght@400;700&family=Roboto+Condensed:ital,wght@0,700;1,700&family=Roboto:wght@400;700;900&display=swap" rel="stylesheet">
<style>
  :root{
    --pink:#e8175d;
    --green:#68bd3b;
    --yellow:#f0e000;
    --blue:#1592d8;
    --blue-dark:#0b6fb0;
    --ink:#222222;
    --mist:#efefef;
    --white:#ffffff;
    --paper:#e9e9e6;
  }
  *{box-sizing:border-box;margin:0;padding:0}
  html,body{width:1200px;height:900px;overflow:hidden}
  body{background:var(--paper);position:relative;font-family:"Lato",sans-serif;color:var(--ink)}

  .postcard{position:absolute;width:690px;height:460px;left:289.5px;transform:scale(.9);transform-origin:0 0;overflow:hidden;box-shadow:0 3px 10px rgba(0,0,0,.18)}
  .postcard--front{top:24px;background:var(--mist)}
  .postcard--back{top:462px;background:var(--white)}
  .postcard__shapes{position:absolute;inset:0;width:690px;height:460px}
  .postcard > *:not(.postcard__shapes){position:absolute}

  .brand-name{font-family:"Roboto",sans-serif;font-weight:700;color:var(--green);white-space:nowrap;display:flex;align-items:center;gap:8px}
  .brand-name__dot{display:inline-block;border-radius:50%;background:var(--green)}

  /* front */
  .front__brand{left:60px;top:28px;font-size:34px}
  .front__brand .brand-name__dot{width:14px;height:14px}
  .front__headline{left:40px;top:80px;width:300px;text-align:center;font-family:"Roboto Condensed",sans-serif;font-weight:700;color:var(--white);line-height:1}
  .front__headline-donate{display:block;font-size:84px;letter-spacing:-1px}
  .front__headline-clothing{display:block;font-size:70px;margin-top:2px}
  .front__tagline{left:40px;top:236px;width:300px;text-align:center;font-family:"Roboto",sans-serif;font-weight:700;font-size:29px;color:var(--yellow)}
  .front__badge{left:326px;top:50px;width:130px;height:130px;border-radius:50%;background:var(--yellow);display:flex;flex-direction:column;align-items:center;justify-content:center;line-height:1;font-family:"Roboto",sans-serif;font-weight:700;color:var(--ink);font-size:20px}
  .front__badge-free{font-family:"Roboto Condensed",sans-serif;font-style:italic;color:var(--pink);font-size:38px;margin-top:4px}
  .front__badge-pickups{font-family:"Roboto Condensed",sans-serif;font-style:italic;color:var(--pink);font-size:26px}
  .front__body{left:40px;top:296px;width:330px;text-align:center;font-size:16px;line-height:21px;color:var(--ink)}
  .front__brand-foot{left:400px;top:418px;font-size:20px}
  .front__brand-foot .brand-name__dot{width:10px;height:10px}

  .call-tag{background:var(--yellow);border-radius:10px;font-family:"Roboto Condensed",sans-serif;font-style:italic;font-weight:700;color:var(--ink);text-align:center;white-space:nowrap}
  .phone-pill{display:flex;align-items:center;background:var(--blue);border-radius:26px;color:var(--white);font-family:"Roboto",sans-serif;font-weight:700;box-shadow:0 2px 0 var(--blue-dark)}
  .phone-pill__icon{flex:none;border-radius:50%;background:var(--white);display:flex;align-items:center;justify-content:center;border:3px solid var(--blue)}
  .phone-pill__number{flex:1;text-align:center;letter-spacing:.5px}

  .front__call{left:108px;top:369px;width:232px;height:22px;font-size:15px;line-height:22px}
  .front__phone{left:40px;top:390px;width:328px;height:50px;font-size:36px}
  .front__phone .phone-pill__icon{width:50px;height:50px}

  /* back */
  .back__stamp{left:586px;top:9px;width:96px;height:96px;background:#dedede;border:1px dashed #b5b5b5}
  .back__brand{left:86px;top:126px;font-size:30px}
  .back__brand .brand-name__dot{width:13px;height:13px}
  .back__intro{left:58px;top:183px;width:250px;font-family:"Roboto",sans-serif;font-size:10.5px;line-height:13px;color:var(--ink)}
  .back__intro p + p{margin-top:12px}
  .back__intro-name{color:var(--green);font-weight:700}
  .back__appeal{left:60px;top:286px;width:258px;text-align:right;font-family:"Roboto",sans-serif;font-weight:700;font-size:19px;line-height:25px;color:var(--blue)}
  .back__appeal-accent{color:var(--pink)}
  .back__call{left:112px;top:372px;width:214px;height:20px;font-size:14px;line-height:20px}
  .back__phone{left:46px;top:390px;width:300px;height:47px;font-size:32px}
  .back__phone .phone-pill__icon{width:47px;height:47px}
</style>
</head>
<body>

<section class="postcard postcard--front" aria-label="Postcard front">
  <svg class="postcard__shapes" viewBox="0 0 690 460" aria-hidden="true">
    <path d="M0 0H690V300C610 300 470 270 380 268C250 265 90 275 0 288Z" fill="var(--pink)"/>
    <path d="M0 288C90 275 250 265 380 268C470 270 560 285 640 300L640 308C560 294 470 282 380 281C250 280 110 290 0 300Z" fill="var(--yellow)"/>
    <path d="M690 330C620 360 560 420 540 460H690Z" fill="var(--yellow)"/>
    <path d="M690 320C655 335 630 360 615 380C650 372 675 360 690 356Z" fill="var(--green)"/>
    <circle cx="548" cy="178" r="190" fill="var(--pink)"/>
  </svg>
  <svg class="postcard__shapes" viewBox="0 0 690 460" role="img" aria-label="Illustration of a smiling child with a backpack running down a sunny town street with friends">
    <defs>
      <linearGradient id="scene-tone" x1="0" y1="0" x2="1" y2="1">
        <stop offset="0" stop-color="#e9b98a"/>
        <stop offset=".55" stop-color="#b77a4f"/>
        <stop offset="1" stop-color="#3f8fc0"/>
      </linearGradient>
    </defs>
    <circle cx="548" cy="172" r="178" fill="url(#scene-tone)"/>
  </svg>

  <div class="brand-name front__brand"><span class="brand-name__dot"></span>Bright Path Youth</div>
  <h1 class="front__headline">
    <span class="front__headline-donate">DONATE</span>
    <span class="front__headline-clothing">CLOTHING</span>
  </h1>
  <p class="front__tagline">-Change Lives!</p>
  <div class="front__badge">
    <span>We offer</span>
    <span class="front__badge-free">FREE</span>
    <span class="front__badge-pickups">Pickups</span>
  </div>
  <p class="front__body">Your gently used clothing can fund life-changing programs and provide hope to those who need it most.</p>
  <p class="call-tag front__call">Call us to schedule your pickup</p>
  <div class="phone-pill front__phone">
    <span class="phone-pill__icon">
      <svg width="26" height="26" viewBox="0 0 24 24" aria-hidden="true"><path d="M6.6 10.8a15.1 15.1 0 0 0 6.6 6.6l2.2-2.2a1 1 0 0 1 1-.25 11.4 11.4 0 0 0 3.6.57 1 1 0 0 1 1 1V20a1 1 0 0 1-1 1A17 17 0 0 1 3 4a1 1 0 0 1 1-1h3.5a1 1 0 0 1 1 1c0 1.25.2 2.45.57 3.57a1 1 0 0 1-.25 1Z" fill="var(--blue)"/></svg>
    </span>
    <span class="phone-pill__number">555-014-2387</span>
  </div>
  <div class="brand-name front__brand-foot"><span class="brand-name__dot"></span>Bright Path Youth</div>
</section>

<section class="postcard postcard--back" aria-label="Postcard back">
  <svg class="postcard__shapes" viewBox="0 0 690 460" aria-hidden="true">
    <path d="M0 0H100C40 80 20 200 60 300C100 390 230 440 345 460H0Z" fill="var(--pink)"/>
    <path d="M100 0C40 80 20 200 60 300C100 390 230 440 345 460" fill="none" stroke="var(--green)" stroke-width="3"/>
    <path d="M260 460C290 450 320 446 345 440L345 460Z" fill="var(--green)"/>
  </svg>
  <div class="back__stamp" aria-label="Stamp area"></div>
  <div class="brand-name back__brand"><span class="brand-name__dot"></span>Bright Path Youth</div>
  <div class="back__intro">
    <p><span class="back__intro-name">Bright Path Youth</span> is a nonprofit organization providing meals and medical services to children in need across Honduras.</p>
    <p>Your gently used clothing can fund life - changing programs and provide hope to those who need it most.</p>
  </div>
  <p class="back__appeal">Give the <span class="back__appeal-accent">gift of care today</span><br>your donation makes<br>a difference!</p>
  <p class="call-tag back__call">Call us to schedule your pickup</p>
  <div class="phone-pill back__phone">
    <span class="phone-pill__icon">
      <svg width="24" height="24" viewBox="0 0 24 24" aria-hidden="true"><path d="M6.6 10.8a15.1 15.1 0 0 0 6.6 6.6l2.2-2.2a1 1 0 0 1 1-.25 11.4 11.4 0 0 0 3.6.57 1 1 0 0 1 1 1V20a1 1 0 0 1-1 1A17 17 0 0 1 3 4a1 1 0 0 1 1-1h3.5a1 1 0 0 1 1 1c0 1.25.2 2.45.57 3.57a1 1 0 0 1-.25 1Z" fill="var(--blue)"/></svg>
    </span>
    <span class="phone-pill__number">555-014-2387</span>
  </div>
</section>

</body>
</html>
```